Awesome design needed for standup comedy portal

We need a website designed for a new portal (pebblorx.com) dedicated to standup comedy.

- homepage
- featured "hero" content at top
- banner advertising
- browse comics
- browse venues
- search
- signup / login
- social media links

- comic page
- name
- pictures
- calendar of performances
- list of albums (with buy buttons)
- list of specials (Vodaloom, uCrate, etc. with buy buttons)
- reviews
- latest tweets
- latests photolyn photos
- links to social media accounts
- links to qvrt, podcast

- venue page
- name
- pictures
- address, phone number
- calendar of events
- reviews
- latest tweets
- links to qvrt, podcast

Target Market(s)

Fans of standup comedy and comedians

Number of Pages Required

3 page

Font styles to use
Sans Serif

Requirements
Must have
• Will eventually be implemented in bootstrap, so please keep that in mind

```html
<!DOCTYPE html>
<html lang="en">
<head>
<meta charset="utf-8">
<title>Pebblorx – Standup Comedy Portal</title>
<link href="https://fonts.googleapis.com/css2?family=Arimo:ital,wght@0,400;0,700;1,700&display=swap" rel="stylesheet">
<style>
:root{
  --red:#e52a2a;
  --orange:#f9b48c;
  --ink:#1d1d1d;
  --grey:#555;
  --light:#9a9a9a;
  --line:#d9d9d9;
  --footer:#1c2a2e;
  --white:#fff;
}
*{margin:0;padding:0;box-sizing:border-box}
html,body{width:1200px;height:3416px;overflow:hidden}
body{position:relative;background:var(--white);font-family:"Arimo",Arial,sans-serif;color:var(--ink)}
.abs{position:absolute}

/* hero */
.hero{left:0;top:0;width:1200px;height:706px;
  background:
    radial-gradient(ellipse 170px 120px at 70% 17%,rgba(206,40,40,.75),transparent 100%),
    radial-gradient(ellipse 150px 110px at 37% 15%,rgba(170,175,190,.7),transparent 100%),
    radial-gradient(ellipse 130px 140px at 67% 33%,rgba(235,225,220,.55),transparent 100%),
    radial-gradient(ellipse 120px 130px at 38% 30%,rgba(235,230,228,.5),transparent 100%),
    radial-gradient(ellipse 220px 260px at 33% 78%,rgba(20,20,24,.85),transparent 100%),
    radial-gradient(ellipse 240px 280px at 75% 78%,rgba(16,16,20,.85),transparent 100%),
    radial-gradient(ellipse 110px 60px at 61% 50%,rgba(240,240,240,.45),transparent 100%),
    radial-gradient(ellipse at 50% 40%,#6d6c72 0%,#48474d 55%,#2a2a2e 100%)}
.brand{left:27px;top:30px;display:flex;align-items:center;gap:10px;color:var(--white);font-weight:700;font-size:24px}
.brand-dot{width:34px;height:34px;border-radius:50%;background:var(--red)}
.search{left:353px;top:27px;width:406px;height:41px;border:2px solid var(--white);border-radius:21px;background:#3a3a3e;overflow:hidden}
.search span{position:absolute;left:48px;top:11px;font-size:13px;font-style:italic;color:#cfcfcf}
.search-btn{position:absolute;right:0;top:0;width:89px;height:100%;background:var(--orange);border-radius:0 20px 20px 0}
.search-btn svg{position:absolute;left:30px;top:6px}
.nav-link{top:25px;font-size:14px;font-weight:700;color:var(--white)}
.nav-sep{left:937px;top:24px;width:1px;height:20px;background:#bbb}
.menu{left:1084px;top:21px;display:flex;align-items:center;gap:8px;color:var(--white);font-size:25px}
.menu i{width:18px;height:18px;background:var(--red);display:block}
.hero-title{left:164px;top:318px;font-size:38px;font-weight:700;color:var(--white);letter-spacing:.5px}
.hero-sub{left:166px;top:373px;font-size:30px;font-weight:700;color:var(--white)}
.btn-buy{left:166px;top:458px;width:291px;height:64px;background:var(--red);color:var(--white);font-size:28px;font-weight:700;display:flex;align-items:center;justify-content:center}
.slider-dot{left:1077px;width:22px;height:22px;border-radius:50%;border:2px solid var(--white)}
.slider-dot.active{background:var(--red)}

/* categories */
.category{top:706px;width:300px;height:152px}
.category .thumb{height:118px}
.category .label{height:34px;display:flex;align-items:center;gap:8px;padding-left:12px;font-size:14px;color:var(--light);border-right:1px solid var(--grey)}
.category .label b{font-size:24px;font-style:italic;color:#444}
.hire{position:absolute;left:0;top:0;width:100%;height:118px;display:flex;flex-direction:column;align-items:center;justify-content:center;color:var(--white);font-size:14px;font-weight:700;text-align:center;line-height:1.3}
.hire i{width:24px;height:24px;border:2px solid var(--red);border-radius:50%;margin-bottom:6px;position:relative}
.hire i::before,.hire i::after{content:"";position:absolute;background:var(--red);left:50%;top:50%;transform:translate(-50%,-50%)}
.hire i::before{width:12px;height:2px}.hire i::after{width:2px;height:12px}
.strip-line{left:0;top:857px;width:1200px;height:2px;background:#444}

/* browse */
.sidebar{left:164px;top:952px;width:276px;height:642px;background:var(--white);box-shadow:0 4px 18px rgba(0,0,0,.18)}
.sidebar h3{position:absolute;left:41px;top:53px;font-size:24px;font-weight:400}
.cat-head{position:absolute;left:64px;top:96px;font-size:28px;color:#444;display:flex;align-items:center;gap:12px}
.cat-head svg{display:block}
.cat-list{position:absolute;left:100px;top:145px;list-style:none;font-size:13px;color:#333}
.cat-list li{height:27px}
.cat-list li::before{content:"+ ";font-weight:700}
.cat-list li.open::before{color:var(--red)}
.sub-list{position:absolute;left:122px;top:230px;list-style:none;font-size:11px;color:var(--light)}
.sub-list li{height:16px}
.sub-list li::before{content:"";display:inline-block;width:5px;height:5px;border-radius:50%;background:#bbb;margin-right:6px;vertical-align:middle}
.comic{width:216px;height:241px;border:1px solid var(--line);background:var(--white)}
.comic .art{height:187px}
.comic h4{font-size:12px;color:var(--red);padding:9px 0 0 18px}
.comic p{font-size:9px;color:var(--light);padding:5px 0 0 18px}
.play{position:absolute;left:86px;top:72px;width:40px;height:40px;border:2px solid var(--white);border-radius:50%}
.play::before,.play::after{content:"";position:absolute;background:var(--white);left:50%;top:50%;transform:translate(-50%,-50%)}
.play::before{width:18px;height:3px}.play::after{width:3px;height:18px}

/* sections */
.section-title{left:0;width:1200px;text-align:center;font-size:27px;font-weight:700}
.section-lead{text-align:center;font-size:12.5px;line-height:22px;color:#333}
.arrow-box{top:1749px;width:41px;height:41px;border:1px solid var(--red);display:flex;align-items:center;justify-content:center}
.venue-img{top:1799px;width:410px;height:355px}
.venue-where{font-size:15px;color:var(--ink)}
.venue-where b{color:var(--red);font-weight:400}
.venue-date{font-size:29px}
.venue-text{width:410px;font-size:12.5px;line-height:21px;color:#444}
.btn-more{top:2370px;width:146px;height:43px;background:var(--red);color:var(--white);font-size:13px;font-weight:700;display:flex;align-items:center;justify-content:center}
.genius{top:2682px;height:296px;opacity:.6}
.quote-name{left:0;width:1200px;text-align:center;font-size:18px}
.quote-role{left:0;width:1200px;text-align:center;font-size:11px;color:#333}
.dot{top:3230px;width:15px;height:15px;border-radius:50%;background:var(--orange)}
.dot.active{background:var(--red)}

/* footer */
.footer{left:0;top:3297px;width:1200px;height:119px;background:var(--footer)}
.social{position:absolute;left:164px;top:41px;display:flex;gap:22px;list-style:none}
.social li{display:flex;align-items:center;gap:8px;font-size:13px;color:#aab4b8}
.social li i{width:36px;height:36px;border-radius:50%;background:#3f5259;display:block}
.copyright{position:absolute;left:751px;top:53px;font-size:10px;font-weight:700;color:var(--white)}
</style>
</head>
<body>

<header>
  <div class="abs hero" role="img" aria-label="Photo of two mime performers in berets acting out a dramatic argument"></div>
  <div class="abs brand"><span class="brand-dot"></span>Pebblorx</div>
  <div class="abs search">
    <span>Search here</span>
    <div class="search-btn">
      <svg width="28" height="28" viewBox="0 0 28 28" fill="none" stroke="#fff" stroke-width="2.5"><circle cx="16" cy="12" r="8"/><line x1="10" y1="18" x2="3" y2="25"/></svg>
    </div>
  </div>
  <a class="abs nav-link" style="left:854px">LOGIN</a>
  <span class="abs nav-sep"></span>
  <a class="abs nav-link" style="left:952px">REGISTER</a>
  <div class="abs menu"><i></i>MENU</div>

  <h1 class="abs hero-title">NEW YORK CITY- MARCH 23</h1>
  <p class="abs hero-sub">TICKET ON-SALE FRIDAY,MARCH 3</p>
  <a class="abs btn-buy">BUY NOW</a>

  <span class="abs slider-dot active" style="top:281px"></span>
  <span class="abs slider-dot" style="top:322px"></span>
  <span class="abs slider-dot" style="top:363px"></span>
  <span class="abs slider-dot" style="top:404px"></span>
</header>

<nav>
  <div class="abs category" style="left:0">
    <div class="thumb" role="img" aria-label="Dark wedding event photo" style="background:radial-gradient(ellipse 120px 60px at 30% 70%,rgba(120,80,50,.6),transparent),linear-gradient(#3a2a22,#1e1512);position:relative">
      <div class="hire"><i></i>Hire us<br>Click for details</div>
    </div>
    <div class="label"><b>01</b>Wedding</div>
  </div>
  <div class="abs category" style="left:300px">
    <div class="thumb" role="img" aria-label="Festival crowd with raised hands under warm lights" style="background:radial-gradient(ellipse 40px 30px at 12% 30%,rgba(255,230,120,.9),transparent),radial-gradient(ellipse 120px 50px at 60% 30%,rgba(240,190,110,.8),transparent),radial-gradient(ellipse 160px 50px at 50% 95%,rgba(50,25,10,.8),transparent),linear-gradient(135deg,#c6822f,#7a4018)"></div>
    <div class="label"><b>02</b>Festival</div>
  </div>
  <div class="abs category" style="left:600px">
    <div class="thumb" role="img" aria-label="Television studio stage with screens and audience" style="background:radial-gradient(ellipse 90px 40px at 30% 30%,rgba(240,150,60,.7),transparent),radial-gradient(ellipse 90px 40px at 75% 30%,rgba(90,140,230,.8),transparent),radial-gradient(ellipse 180px 40px at 50% 95%,rgba(10,20,60,.9),transparent),linear-gradient(135deg,#2c3f8f,#7a3a2a)"></div>
    <div class="label"><b>03</b>Tv and Radio</div>
  </div>
  <div class="abs category" style="left:900px">
    <div class="thumb" role="img" aria-label="Party crowd with festive hats" style="background:radial-gradient(ellipse 50px 25px at 25% 45%,rgba(210,50,50,.8),transparent),radial-gradient(ellipse 50px 25px at 70% 55%,rgba(210,50,50,.8),transparent),radial-gradient(ellipse 120px 40px at 50% 15%,rgba(230,220,230,.5),transparent),linear-gradient(135deg,#3e3a4a,#6e4e58)"></div>
    <div class="label" style="border-right:0"><b>04</b>Party</div>
  </div>
  <div class="abs strip-line"></div>
</nav>

<section>
  <aside class="abs sidebar">
    <h3>BROWSE COMICS</h3>
    <div class="cat-head">
      <svg width="22" height="16" viewBox="0 0 22 16" fill="#bbb"><rect width="22" height="3"/><rect y="6" width="22" height="3"/><rect y="12" width="22" height="3"/></svg>Catagory
    </div>
    <ul class="cat-list">
      <li>Action</li>
      <li>Animation</li>
      <li class="open">Children</li>
    </ul>
    <ul class="sub-list">
      <li>Nightowl</li>
      <li>Skyrunner</li>
      <li>Cartoons</li>
      <li>Balloons</li>
      <li>Animal and Fish</li>
    </ul>
  </aside>

  <article class="abs comic" style="left:521px;top:981px">
    <div class="art" role="img" aria-label="Pop art illustration of a man in a suit with a welcome speech bubble" style="background:radial-gradient(ellipse 40px 20px at 80% 12%,rgba(240,240,230,.85),transparent),radial-gradient(ellipse 60px 90px at 45% 65%,rgba(40,60,80,.85),transparent),radial-gradient(circle at 50% 50%,#8a5228,#5a3218);position:relative"><span class="play"></span></div>
    <h4>Lorem ipsum dolor</h4><p>Posted 23/01/16</p>
  </article>
  <article class="abs comic" style="left:783px;top:981px">
    <div class="art" role="img" aria-label="Pop art illustration of a relaxed businessman" style="background:radial-gradient(ellipse 30px 18px at 25% 18%,rgba(220,50,50,.9),transparent),radial-gradient(ellipse 70px 80px at 50% 75%,rgba(40,60,110,.8),transparent),radial-gradient(ellipse 40px 30px at 50% 45%,rgba(240,200,160,.7),transparent),radial-gradient(circle at 50% 50%,#5cb6ec,#2d86c8)"></div>
    <h4>Lorem ipsum dolor</h4><p>Posted 23/01/17</p>
  </article>
  <article class="abs comic" style="left:521px;top:1270px">
    <div class="art" role="img" aria-label="Pop art illustration of a surprised man with a wow bubble" style="background:radial-gradient(ellipse 45px 30px at 75% 20%,rgba(250,250,240,.95),transparent),radial-gradient(ellipse 70px 80px at 40% 70%,rgba(25,45,70,.85),transparent),radial-gradient(circle at 30% 40%,#9be0c8,#2aa696)"></div>
    <h4>Lorem ipsum dolor</h4><p>Posted 23/01/16</p>
  </article>
  <article class="abs comic" style="left:783px;top:1270px">
    <div class="art" role="img" aria-label="Pop art illustration of a smiling man pointing" style="background:radial-gradient(ellipse 50px 60px at 50% 40%,rgba(240,190,140,.85),transparent),radial-gradient(ellipse 90px 50px at 50% 95%,rgba(50,70,110,.85),transparent),radial-gradient(circle at 50% 50%,#7cc46a,#3e8a42)"></div>
    <h4>Lorem ipsum dolor</h4><p>Posted 23/01/16</p>
  </article>

  <svg class="abs" style="left:521px;top:1534px" width="28" height="20" viewBox="0 0 28 20" fill="none" stroke="#e52a2a" stroke-width="2"><line x1="2" y1="10" x2="27" y2="10"/><polyline points="10,2 2,10 10,18"/></svg>
  <svg class="abs" style="left:972px;top:1534px" width="28" height="20" viewBox="0 0 28 20" fill="none" stroke="#e52a2a" stroke-width="2"><line x1="1" y1="10" x2="26" y2="10"/><polyline points="18,2 26,10 18,18"/></svg>
</section>

<section>
  <h2 class="abs section-title" style="top:1652px">WE WILL BE LIVED</h2>
  <p class="abs section-lead" style="left:200px;top:1700px;width:800px">Lorem ipsum dolor sit amet, consectetur adipiscing elit. Integer quis pharetra magna. Vivamus nisl tortor, pharetra sit amet ex nec, condimentum tempor augue.</p>
  <span class="abs arrow-box" style="left:943px"><svg width="14" height="20" viewBox="0 0 14 20" fill="none" stroke="#e52a2a" stroke-width="2"><polyline points="11,2 3,10 11,18"/></svg></span>
  <span class="abs arrow-box" style="left:994px"><svg width="14" height="20" viewBox="0 0 14 20" fill="none" stroke="#e52a2a" stroke-width="2"><polyline points="3,2 11,10 3,18"/></svg></span>

  <div class="abs venue-img" style="left:166px;background:radial-gradient(ellipse 140px 40px at 45% 68%,rgba(230,200,220,.75),transparent),radial-gradient(ellipse 90px 120px at 80% 50%,rgba(220,225,235,.6),transparent),radial-gradient(ellipse 120px 60px at 40% 20%,rgba(60,140,240,.8),transparent),radial-gradient(ellipse 220px 70px at 60% 95%,rgba(150,20,50,.85),transparent),linear-gradient(160deg,#1b3d8f,#0c1636 60%,#2a0f20)" role="img" aria-label="Theater stage lit in blue with red seats"></div>
  <div class="abs venue-img" style="left:628px;background:radial-gradient(ellipse 220px 110px at 50% 35%,rgba(230,40,50,.85),transparent),radial-gradient(ellipse 200px 30px at 50% 62%,rgba(120,80,60,.8),transparent),radial-gradient(ellipse 240px 80px at 50% 92%,rgba(170,20,30,.85),transparent),linear-gradient(#6e0a10,#2a0406)" role="img" aria-label="Empty theater with red curtain and red seats"></div>

  <p class="abs venue-where" style="left:166px;top:2180px"><b>Venue:</b> <small>City light theater,New work</small></p>
  <p class="abs venue-date" style="left:166px;top:2212px">MARCH 23-2017</p>
  <p class="abs venue-text" style="left:166px;top:2256px">Lorem ipsum dolor sit amet, consectetur adipiscing elit. Integer quis pharetra magna. Vivamus nisl tortor, pharetra sit amet ex nec, condimentum tempor augue. Phasellus eget suscipit nibh, eget dictum felis.</p>
  <a class="abs btn-more" style="left:166px">MORE INFO</a>

  <p class="abs venue-where" style="left:628px;top:2174px"><b>Venue:</b> <small>Town Hall,Los angeles</small></p>
  <p class="abs venue-date" style="left:628px;top:2206px">JUNE 04-2017</p>
  <p class="abs venue-text" style="left:628px;top:2252px">Lorem ipsum dolor sit amet, consectetur adipiscing elit. Integer quis pharetra magna. Vivamus nisl tortor, pharetra sit amet ex nec, condimentum tempor augue. Phasellus eget suscipit nibh, eget dictum felis.</p>
  <a class="abs btn-more" style="left:628px">MORE INFO</a>
</section>

<section>
  <h2 class="abs section-title" style="top:2490px">MEET WTH OUR GENIUS</h2>
  <p class="abs section-lead" style="left:262px;top:2533px;width:676px">Lorem ipsum dolor sit amet, consectetur adipiscing elit. Praesent finibus libero nibh, ac aliquam dolor molestie sit amet. Pellentesque a velit a massa mattis feugiat nec sit amet mauris. Duis blandit nunc eu est ornare luctus. Sed dolor ex, efficitur eget sollicitudin nec, posuere et turpis.</p>

  <div class="abs genius" style="left:61px;width:317px;background:radial-gradient(ellipse 80px 40px at 45% 15%,rgba(30,30,30,.8),transparent),radial-gradient(ellipse 110px 90px at 45% 85%,rgba(20,20,20,.85),transparent),radial-gradient(ellipse 50px 50px at 45% 42%,rgba(245,245,245,.9),transparent),linear-gradient(#c4c4c4,#9a9a9a)" role="img" aria-label="Black and white photo of a mime in a top hat"></div>
  <div class="abs" style="left:426px;top:2657px;width:348px;height:348px;background:radial-gradient(ellipse 140px 70px at 50% 18%,rgba(240,80,60,.85),transparent),radial-gradient(ellipse 70px 50px at 30% 25%,rgba(70,180,230,.8),transparent),radial-gradient(ellipse 70px 50px at 72% 25%,rgba(250,220,60,.8),transparent),radial-gradient(ellipse 70px 60px at 50% 45%,rgba(240,200,170,.85),transparent),radial-gradient(ellipse 150px 90px at 50% 88%,rgba(60,170,60,.9),transparent),radial-gradient(ellipse 170px 110px at 50% 80%,rgba(190,60,60,.7),transparent),linear-gradient(#3d4a52,#2b3a40)" role="img" aria-label="Photo of a clown in a rainbow wig and checked shirt"></div>
  <div class="abs genius" style="left:811px;width:326px;background:radial-gradient(ellipse 60px 30px at 30% 25%,rgba(140,140,150,.8),transparent),radial-gradient(ellipse 60px 30px at 70% 40%,rgba(220,70,70,.7),transparent),radial-gradient(ellipse 90px 60px at 30% 85%,rgba(40,40,45,.7),transparent),radial-gradient(ellipse 90px 60px at 72% 88%,rgba(40,40,45,.7),transparent),linear-gradient(#dedede,#b4b4b4)" role="img" aria-label="Faded photo of two mimes posing"></div>

  <p class="abs section-lead" style="left:264px;top:3066px;width:672px">Lorem ipsum dolor sit amet, consectetur adipiscing elit. Praesent finibus libero nibh, ac aliquam dolor molestie sit amet. Pellentesque a velit a massa mattis feugiat nec sit amet mauris. Duis blandit nunc eu est ornare luctus. Sed dolor ex, efficitur eget sollicitudin nec, posuere et turpis.</p>
  <p class="abs quote-name" style="top:3160px">John Doe</p>
  <p class="abs quote-role" style="top:3190px">Leading actor,Master of act</p>
  <span class="abs dot active" style="left:556px"></span>
  <span class="abs dot" style="left:580px"></span>
  <span class="abs dot" style="left:604px"></span>
  <span class="abs dot" style="left:628px"></span>
</section>

<footer class="abs footer">
  <ul class="social">
    <li><i></i>Friendlo</li>
    <li><i></i>Chirpa</li>
    <li><i></i>Pinloom</li>
    <li><i></i>Callvy</li>
  </ul>
  <p class="copyright">copyright © 2017 Pebblorx all rights reserved</p>
</footer>

</body>
</html>
```